Our company TrulaPay, an online processor of payments is seeking talented submissions for our website redesign. The winning design will be chopped up and converted into a WordPress theme to allow for easy content additions and updates.

We are looking for modern designs that rival current websites in our industry (plimo.example, zanquetto.example, holvix.example, brandle.example, quillmarkcharges.example, evensplitcharges.example, KoboRun.example).

Our company is seeking to expand our reach to software developers and engineers who are either integrating our payment platform into their offerings or are engineering a custom solution for the company they work for and are in need of a payment platform such as our own.

We currently work with hundreds of different business partners whom either resell our services or integrate our processing capabilities into their software (which they sell). We also must communicate effectively to end users, businesses, who seek us out directly for their payment processing needs.

We are open to different color schemes but would ultimately like them to be somewhat inline with our current logo (see attached). Our website needs to instill security and confidence to any current and/or potential user as we are trusted with private and sensitive information.

We are seeking submissions from qualified; individual freelancers, freelance teams, and agencies who can attack this project in its entirety. Since this project is a total redesign, we would like submissions that have the capability to design any custom graphics, icons, buttons, and illustrations in line with our industry, capabilities, offerings, and content. We are looking for someone to design our new website and would prefer a vendor who can also help us to design elements (graphics, illustrations, charts, workflows) within our website.

Designs will be converted into a wordpress theme and we would like to utilize widgets for as many areas as possible to make editing and updating easy.

We are seeking the creation of a few unique pages but many of the pages for the majority of our content will just be internal content pages which will be duplicated.

We will likely contract with the winning submission for future work.

Please see Design Reference Document for more information

Target Market(s)

Resellers
Merchant Service Providers
Software Developers
Independent Sales Organizations (ISOs)
App Builders
Mobile App Builders
Independent Software Developers
Organizational Software Developers
Businesses who need to accept payments
Governments
Municipalities
Schools
DMVs
Courts
Retailers
Medical Offices
Hosipitals
Clinics
Dr. Offices
Gyms
Churches
Non-Profits
Software Companies
Technology Companies
Startups

• Logo cannot change drastically.

```html
<!DOCTYPE html>
<html lang="en">
<head>
<meta charset="utf-8">
<title>TrulaPay — Happiness begins with TrulaPay</title>
<link rel="stylesheet" href="https://fonts.googleapis.com/css2?family=Open+Sans:wght@400;600;700&display=swap">
<style>
  :root {
    --navy: #1d2a8c;
    --purple: #9a5cb4;
    --orange: #f4a210;
    --blue: #3597db;
    --slate: #354657;
    --red: #e74c3c;
    --green: #1db86a;
    --green-light: #2fd17f;
    --footer: #3a4655;
    --mint: #34d47b;
    --white: #ffffff;
    --ink: #111111;
    --device-grey: #8f9193;
    --device-screen: #f25d5d;
    --bar-dark: #3a4552;
  }
  * { box-sizing: border-box; margin: 0; padding: 0; }
  html, body { width: 937px; height: 1200px; overflow: hidden; background: var(--white); }
  body { font-family: "Open Sans", sans-serif; color: var(--white); }
  .page { position: relative; width: 937px; height: 1200px; overflow: hidden; }

  /* Hero */
  .hero { position: absolute; left: 0; top: 0; width: 937px; height: 517px; }
  .hero-photo {
    position: absolute; inset: 0;
    background:
      radial-gradient(ellipse at 30% 55%, #e8c3ad 0%, rgba(232,195,173,0) 45%),
      radial-gradient(ellipse at 72% 60%, #b8866b 0%, rgba(184,134,107,0) 40%),
      linear-gradient(180deg, #dfe6ee 0%, #c9d3dd 45%, #aebbc8 100%);
  }
  .brand {
    position: absolute; left: 38px; top: 34px;
    display: flex; align-items: center; gap: 7px;
    font-size: 30px; font-weight: 700; color: var(--navy); letter-spacing: -0.5px;
  }
  .brand-dot { width: 10px; height: 10px; border-radius: 50%; background: var(--navy); }
  .main-nav {
    position: absolute; left: 306px; top: 34px; width: 631px; height: 41px;
    background: var(--purple);
  }
  .main-nav a {
    position: absolute; top: 11px; transform: translateX(-50%);
    color: var(--white); text-decoration: none; font-size: 13.5px; white-space: nowrap;
  }
  .hero-title {
    position: absolute; left: 68px; top: 238px;
    font-size: 43px; font-weight: 400; color: var(--white); letter-spacing: -0.3px;
  }

  /* Sub navigation */
  .sub-nav { position: absolute; left: 0; top: 517px; width: 937px; height: 42px; background: var(--orange); }
  .sub-nav a {
    position: absolute; top: 8px; color: var(--white); text-decoration: none;
    font-size: 19px; white-space: nowrap;
  }
  .sub-nav a.is-active { color: var(--ink); font-size: 22px; top: 5px; }

  /* Slides */
  .slide { position: absolute; left: 0; width: 937px; overflow: hidden; }
  .slide-mobile { top: 559px; height: 245px; background: var(--blue); }
  .slide-terminal { top: 804px; height: 284px; background: var(--red); }
  .slide-art { position: absolute; left: 0; top: 0; }
  .slide-title { position: absolute; font-size: 17px; font-weight: 700; }
  .slide-text { position: absolute; width: 338px; font-size: 10.4px; line-height: 15px; }
  .device { position: absolute; }
  .device-phone {
    left: 740px; top: 7px; width: 154px; height: 250px; border-radius: 9px;
    background: linear-gradient(180deg, var(--device-screen) 0%, var(--device-screen) 70%, var(--device-grey) 100%);
  }
  .device-tablet {
    left: 6px; top: 54px; width: 248px; height: 176px; border-radius: 10px;
    background: var(--slate);
  }
  .slide-arrows { position: absolute; left: 0; top: 0; }

  /* Footer */
  .footer { position: absolute; left: 0; top: 1088px; width: 937px; height: 112px; background: var(--footer); }
  .footer-divider { position: absolute; top: 15px; width: 1px; height: 73px; background: #d5dbe2; }
  .contact { position: absolute; left: 41px; top: 34px; font-size: 13px; line-height: 17px; }
  .contact h3 { font-size: 13px; font-weight: 700; color: var(--mint); }
  .link-list { position: absolute; list-style: none; font-size: 13px; line-height: 17px; }
  .social {
    position: absolute; width: 40px; height: 36px; border-radius: 5px;
    display: flex; align-items: center; justify-content: center;
    font-size: 7.5px; font-weight: 600; color: var(--white); text-decoration: none;
  }
  .social-chirp { left: 828px; top: 9px; background: #2d9ad8; }
  .social-work { left: 886px; top: 9px; background: #1f6fa8; }
  .social-page { left: 828px; top: 57px; background: #3b5a9a; }
  .social-feed { left: 886px; top: 57px; background: #e6842a; }
</style>
</head>
<body>
<div class="page">

  <header class="hero">
    <div class="hero-photo" role="img" aria-label="Photo of a smiling group of business colleagues"></div>
    <div class="brand"><span>TrulaPay</span><span class="brand-dot"></span></div>
    <nav class="main-nav">
      <a href="#" style="left:34px">Home</a>
      <a href="#" style="left:122px">Solutions</a>
      <a href="#" style="left:218px">Developers</a>
      <a href="#" style="left:327px">Partners</a>
      <a href="#" style="left:421px">Company</a>
      <a href="#" style="left:514px">Resources</a>
      <a href="#" style="left:602px">Blog</a>
    </nav>
    <h1 class="hero-title">Happiness begins with TrulaPay</h1>
  </header>

  <nav class="sub-nav">
    <a href="#" class="is-active" style="left:64px">Overview</a>
    <a href="#" style="left:208px">Libraries</a>
    <a href="#" style="left:328px">Test Account</a>
    <a href="#" style="left:489px">Quick Start</a>
    <a href="#" style="left:625px">Documentation</a>
    <a href="#" style="left:802px">Support</a>
  </nav>

  <section class="slide slide-mobile">
    <svg class="slide-art" width="937" height="245" viewBox="0 0 937 245">
      <circle cx="870" cy="125" r="246" fill="var(--slate)"/>
      <rect x="287" y="226" width="90" height="5" rx="2.5" fill="var(--bar-dark)"/>
      <rect x="409" y="226" width="89" height="5" rx="2.5" fill="#fff"/>
      <rect x="532" y="226" width="90" height="5" rx="2.5" fill="#fff"/>
    </svg>
    <div class="device device-phone" role="img" aria-label="Illustration of a smartphone showing the TrulaPay brand and a Go Mobile message"></div>
    <svg class="slide-arrows" width="937" height="245" viewBox="0 0 937 245">
      <polyline points="41,79 33,96 41,113" fill="none" stroke="#fff" stroke-width="2.5"/>
      <polyline points="891,79 899,96 891,113" fill="none" stroke="#fff" stroke-width="2.5"/>
    </svg>
    <h2 class="slide-title" style="left:121px; top:40px">Mobile</h2>
    <p class="slide-text" style="left:121px; top:66px">Lorem ipsum dolor sit amet, consectetur adipiscing elit. Ut tempor massa in mi dictum vehicula. Nunc porttitor metus orci, ut blandit tellus blandit eget. Phasellus dolor elit, volutpat et euismod in, luc us vel elit. Etiam mi nibh, tincidunt eget hendrerit nec, euismod ve tortor. Proin quis rhoncus arcu. Nunc ut dolor a nibh ornare alique ac at elit. Vestibulum in eros tincidunt nibh pulvinar malesuada ne vitae quam. Integer pretium nunc id consequat aliquam. us a, pla</p>
  </section>

  <section class="slide slide-terminal">
    <svg class="slide-art" width="937" height="284" viewBox="0 0 937 284">
      <defs>
        <linearGradient id="greenFade" x1="0" y1="0" x2="1" y2="1">
          <stop offset="0" stop-color="var(--green-light)"/>
          <stop offset="1" stop-color="var(--green)"/>
        </linearGradient>
      </defs>
      <circle cx="96" cy="144" r="225" fill="url(#greenFade)"/>
      <rect x="287" y="256" width="90" height="5" rx="2.5" fill="#fff"/>
      <rect x="409" y="256" width="89" height="5" rx="2.5" fill="var(--bar-dark)"/>
      <rect x="532" y="256" width="90" height="5" rx="2.5" fill="#fff"/>
    </svg>
    <div class="device device-tablet" role="img" aria-label="Illustration of a tablet used as a virtual terminal"></div>
    <svg class="slide-arrows" width="937" height="284" viewBox="0 0 937 284">
      <polyline points="38,125 30,142 38,159" fill="none" stroke="#fff" stroke-width="2.5"/>
      <polyline points="891,125 899,142 891,159" fill="none" stroke="#fff" stroke-width="2.5"/>
    </svg>
    <h2 class="slide-title" style="left:444px; top:74px">Virtual Terminal</h2>
    <p class="slide-text" style="left:444px; top:100px">Lorem ipsum dolor sit amet, consectetur adipiscing elit. Ut tempor massa in mi dictum vehicula. Nunc porttitor metus orci, ut blandit tellus blandit eget. Phasellus dolor elit, volutpat et euismod in, luc us vel elit. Etiam mi nibh, tincidunt eget hendrerit nec, euismod ve tortor. Proin quis rhoncus arcu. Nunc ut dolor a nibh ornare alique ac at elit. Vestibulum in eros tincidunt nibh pulvinar malesuada ne vitae quam. Integer pretium nunc id consequat aliquam. us a, pla</p>
  </section>

  <footer class="footer">
    <div class="contact">
      <h3>Contact Information</h3>
      <p>Lorem ipsum dolor sit amet, consectetu<br>fringilla. Aenean quis nunc ipsum. Aliqu</p>
    </div>
    <span class="footer-divider" style="left:306px"></span>
    <ul class="link-list" style="left:360px; top:34px">
      <li>ACH Processing</li>
      <li>eCheck Processing</li>
      <li>Paper Check Processing</li>
    </ul>
    <span class="footer-divider" style="left:550px"></span>
    <ul class="link-list" style="left:611px; top:30px">
      <li>ACH Processing</li>
      <li>eCheck Processing</li>
      <li>Paper Check Processing</li>
    </ul>
    <a class="social social-chirp" href="#">Chirpline</a>
    <a class="social social-work" href="#">Workmesh</a>
    <a class="social social-page" href="#">Pagecircle</a>
    <a class="social social-feed" href="#">Feed</a>
  </footer>

</div>
</body>
</html>
```